Old Fashioned, Artisan Goat Milk Soap Label

We are branching out in our goat milk dairy into artisan goat milk soaps. High quality, yet an old fashioned feel. Simple yet elegant. Emphasis on the milk and its moisturizing, healing, softening, and superiority.
Purity in a simple design that harkens back to a quaint, earlier time where quality ingredients were valued as much as quality workmanship.
Perhaps a drop symbolizing the milk, or a bucket pouring into or out of the logo. We already have our farm logo, Willowbrook Hollow, and were thinking the soap would be "Sweet Nell"
The labels will grace our liquid soap bottles and our bar soaps. 3.5" X 2.5"
The label color will be an antiqued ivory or other shade to convey a simpler time.

Reason: Realized that the contest length was short enough to scare away designers. Adding time to give entered designers time to create.

Target Market(s)

Upscale people looking to know where their products come from. People looking for better options, artisan products.

Requirements
Must have
• My project must have emphasis on the milk, old time feel, simple elegance
Nice to have
• Perhaps a drop symbolizing the milk, or a bucket pouring into or out of the logo. We already have our farm logo, Willowbrook Hollow, and were thinking the soap would be "Sweet Nell"
• If you use a goat, please be aware that we have the breed Nubians that have long luxurious ears and don't have horns.

```html
<!DOCTYPE html>
<html lang="en">
<head>
<meta charset="utf-8">
<title>Sweet Nell Goat Milk Soap Label</title>
<link rel="stylesheet" href="https://fonts.googleapis.com/css2?family=Poppins:wght@300;400;600&display=swap">
<style>
  :root {
    --backdrop: #ffffff;
    --ivory: #fbfaf3;
    --pattern-tone: #ecebe2;
    --pattern-edge: #e2e1d6;
    --navy: #1f2a57;
    --rule: #8d8fa3;
    --milk-light: #fdfdfb;
    --milk-shade: #dcdcd6;
  }
  * { box-sizing: border-box; margin: 0; padding: 0; }
  html, body {
    width: 1200px;
    height: 846px;
    overflow: hidden;
    background: var(--backdrop);
    font-family: "Poppins", sans-serif;
    color: var(--navy);
  }
  .canvas {
    width: 1200px;
    height: 846px;
    display: flex;
    align-items: center;
    justify-content: center;
  }
  .label {
    position: relative;
    width: 640px;
    height: 680px;
    display: flex;
    box-shadow: 0 0 0 1px var(--pattern-edge);
  }
  .label__pattern {
    width: 124px;
    height: 100%;
    background: var(--pattern-tone);
  }
  .label__panel {
    flex: 1;
    background: var(--ivory);
    display: flex;
    flex-direction: column;
    align-items: center;
    padding-top: 44px;
  }
  .brand {
    display: flex;
    align-items: center;
    gap: 10px;
    font-weight: 600;
    font-size: 22px;
    letter-spacing: 0.06em;
    text-transform: uppercase;
    color: var(--navy);
  }
  .brand__mark {
    width: 14px;
    height: 14px;
    background: var(--navy);
  }
  .product-name {
    margin-top: 118px;
    font-weight: 300;
    font-size: 54px;
    line-height: 1;
    letter-spacing: 0.01em;
  }
  .product-type {
    margin-top: 22px;
    width: 300px;
    border-top: 1px solid var(--rule);
    border-bottom: 1px solid var(--rule);
    padding: 10px 0 8px;
    text-align: center;
    font-weight: 300;
    font-size: 18px;
  }
  .tagline {
    margin-top: 18px;
    font-weight: 300;
    font-size: 12.5px;
  }
  .milk-drop {
    margin-top: 40px;
    width: 300px;
    height: 180px;
    border-radius: 50%;
    background: radial-gradient(ellipse at 50% 45%, var(--milk-light) 0%, #f1f1ee 45%, var(--milk-shade) 100%);
  }
</style>
</head>
<body>
  <main class="canvas">
    <article class="label">
      <div class="label__pattern" role="img" aria-label="Soft ivory lace-like decorative pattern border"></div>
      <section class="label__panel">
        <div class="brand"><span class="brand__mark"></span>Willowbrook Hollow</div>
        <h1 class="product-name">Sweet Nell</h1>
        <p class="product-type">goat milk soaps</p>
        <p class="tagline">moisturizing, healing, softening, and superiority.</p>
        <div class="milk-drop" role="img" aria-label="Photograph of a milk drop splashing into a pool of milk"></div>
      </section>
      <div class="label__pattern" role="img" aria-label="Soft ivory lace-like decorative pattern border"></div>
    </article>
  </main>
</body>
</html>
```